'Velunor' Nutritional supplements label design (UPDATED)

- 'Velunor' is a upscale health supplements brand
-The company will be packing the products in plastic bottles like other supplements
-Try to use a distinct design which is recognizable from distance
-Brand Logo is attached

-UPDATE- 2-

Label Dimensions and Design:

Hi Everyone,

Sorry for the late response caused by some very busy schedule.

Anyhow, here are the dimensions of the label (Self Adhesive) that we need:

Length of Label : 18cm
Height of Label : 6.5 cm

Product Names:

-Metabolism Formula
-Complete Multivitamins and Minerals (For Men, Women and Kids)
-Healthy Bones
-Skin Support
-Omega-3 oil for Healthy Heart

As for the ingredients just use Lorem Ipsum for now.

Many thanks to all of you in advance.

Target Market(s)

Middle Income families

Industry/Entity Type

Plastic

Requirements
Must have
• -Quality
-Effective
-Unique

```html
<!DOCTYPE html>
<html lang="en">
<head>
<meta charset="utf-8">
<title>Velunor – Label Band</title>
<link href="https://fonts.googleapis.com/css2?family=Jost:wght@500&display=swap" rel="stylesheet">
<style>
  :root {
    --paper: #ffffff;
    --teal: #00cccc;
    --mint: #02fd82;
  }
  html, body {
    margin: 0;
    padding: 0;
    width: 1200px;
    height: 900px;
    overflow: hidden;
    background: var(--paper);
  }
  .label {
    position: relative;
    width: 1200px;
    height: 900px;
  }
  .label__band {
    position: absolute;
    inset: 0;
    display: block;
  }
  .band__teal { fill: var(--teal); }
  .band__mint { fill: var(--mint); }
  .band__window { fill: var(--paper); }
  .brand {
    position: absolute;
    left: 350px;
    top: 380px;
    width: 500px;
    height: 140px;
    display: flex;
    align-items: center;
    justify-content: center;
    gap: 26px;
  }
  .brand__dot {
    width: 58px;
    height: 58px;
    border-radius: 50%;
    background: var(--mint);
    flex: none;
  }
  .brand__name {
    margin: 0;
    font-family: "Jost", "Futura", sans-serif;
    font-weight: 500;
    font-size: 78px;
    letter-spacing: 10px;
    line-height: 1;
    color: var(--teal);
  }
</style>
</head>
<body>
  <main class="label">
    <svg class="label__band" width="1200" height="900" viewBox="0 0 1200 900" aria-hidden="true">
      <rect class="band__teal" x="0" y="233" width="1200" height="132"/>
      <rect class="band__mint" x="0" y="365" width="1200" height="170"/>
      <rect class="band__teal" x="0" y="535" width="1200" height="131"/>
      <polygon class="band__mint" points="350,233 897,233 836,365 290,365"/>
      <polygon class="band__window" points="290,365 836,365 916,535 370,535"/>
      <polygon class="band__mint" points="370,535 916,535 855,666 308,666"/>
    </svg>
    <div class="brand">
      <span class="brand__dot"></span>
      <h1 class="brand__name">VELUNOR</h1>
    </div>
  </main>
</body>
</html>
```